Redesign ideas for already developed financial iOS app

We are looking for design ideas for an app that we have coded, but which needs a fresh look and feel and some improvement of the navigation and UIX (screenshots uploaded).

The app enables investors to rank investment ideas/stocks based on their ethical & spiritual importance to them, and provides users with a resulting overall “Halden Index" for the ranked securities/investments.

Our company, Qubrelo.com has been associated with transparency since 2001 when we made the performance of Wall Street analysts public and helped regulators uncover substantial conflicts of interest.

We subsequently helped investors discover "independent research". Our data on analyst performance is currently provided to millions of investors through our broker partners. Throughout our history we have empowered investors by making the performance of those they get advice from transparent.

The final design should communicate ease, security and simplicity.

IMPORTANT: The main focus of any design proposals should be the "Share Sifter". You can find a screenshot of this screen here again: http://clipvorra.example/t/QM8TwRkDp

Good luck and thank you for joining us in our mission.

Target Market(s)

Retail investors

Industry/Entity Type

Financial

Requirements
Must have
• easy of use, simplcity
Nice to have
• interactive design
Should not have
• over-complicated

```html
<!DOCTYPE html>
<html lang="en">
<head>
<meta charset="utf-8">
<title>Lumenvest – Index Details</title>
<link rel="stylesheet" href="https://fonts.googleapis.com/css2?family=Open+Sans:wght@300;400;600&display=swap">
<style>
  :root{
    --stage:#e6e6e6;
    --brand-blue:#359fd3;
    --screen-bg:#ffffff;
    --list-bg:#f2f2f2;
    --rule:#dcdcdc;
    --text:#555555;
    --text-dark:#222222;
    --muted:#a9a9a9;
    --loss:#f0505a;
    --gain:#8fd14f;
    --loss-fill:#f5999b;
    --gain-fill:#bfe38f;
    --bench-fill:#8cc7ea;
  }
  *{box-sizing:border-box;margin:0;padding:0}
  html,body{width:1200px;height:1000px;overflow:hidden;background:var(--stage)}
  body{position:relative;font-family:"Open Sans",Arial,sans-serif;color:var(--text)}
  .screen{position:absolute;top:249px;width:270px;height:477px;background:var(--screen-bg);overflow:hidden}
  .screen--splash{left:87px;background:var(--brand-blue)}
  .screen--detail-line{left:466px}
  .screen--detail-area{left:839px}

  .status-bar{height:20px;display:flex;align-items:center;justify-content:space-between;padding:0 6px;font-size:10.5px;color:var(--text-dark);position:relative}
  .screen--splash .status-bar{color:#fff}
  .status-bar .signal{display:flex;align-items:center;gap:3px}
  .status-bar .dots{letter-spacing:-1px}
  .status-bar .time{font-weight:600;position:absolute;left:0;right:0;text-align:center;pointer-events:none}
  .status-bar .battery{display:flex;align-items:center;gap:3px}
  .battery-icon{width:20px;height:9px;border:1px solid currentColor;border-radius:2px;padding:1px}
  .battery-icon span{display:block;height:100%;background:currentColor}

  .splash-brand{position:absolute;left:0;right:0;top:224px;text-align:center;color:#fff}
  .splash-brand .name{font-size:28px;font-weight:300;letter-spacing:.5px;line-height:1}
  .splash-brand .tagline{font-size:9.5px;font-weight:400;margin-top:5px}

  .nav-bar{height:34px;position:relative;display:flex;align-items:center;justify-content:center;font-size:14px;color:var(--text-dark)}
  .nav-bar .back{position:absolute;left:16px;top:10px}
  .index-banner{height:50px;background:var(--brand-blue);color:#fff;font-size:14px;display:flex;align-items:center;padding-left:20px}
  .chart{display:block;width:270px;height:153px}
  .chart text{font-family:"Open Sans",Arial,sans-serif}

  .tabs{height:35px;border-top:1px solid var(--brand-blue);border-bottom:1px solid var(--brand-blue);display:flex;align-items:center;font-size:12px;color:var(--muted)}
  .tabs .tab{flex:1;text-align:center;line-height:1.05}
  .tabs .tab--active{color:var(--brand-blue)}

  .stats{background:var(--list-bg);height:200px;padding:3px 8px 0}
  .stats .row{height:38px;display:flex;align-items:center;justify-content:space-between;padding:0 4px;border-bottom:1px solid var(--rule);font-size:12px;color:var(--text)}
  .stats .loss{color:var(--loss)}
  .stats .gain{color:var(--gain)}
</style>
</head>
<body>

<section class="screen screen--splash">
  <div class="status-bar">
    <span class="signal"><span class="dots">●●●●●</span> Carrier
      <svg width="10" height="8" viewBox="0 0 10 8"><path d="M1 3 Q5 -0.5 9 3 M2.5 4.6 Q5 2.4 7.5 4.6" fill="none" stroke="currentColor" stroke-width="1"/><circle cx="5" cy="6.6" r="1" fill="currentColor"/></svg></span>
    <span class="time">9:41 AM</span>
    <span class="battery">100% <span class="battery-icon"><span></span></span></span>
  </div>
  <div class="splash-brand">
    <div class="name">Lumenvest</div>
    <div class="tagline">Because values are the ONLY measure</div>
  </div>
</section>

<section class="screen screen--detail-line">
  <div class="status-bar">
    <span class="signal"><span class="dots">●●●●●</span> Carrier
      <svg width="10" height="8" viewBox="0 0 10 8"><path d="M1 3 Q5 -0.5 9 3 M2.5 4.6 Q5 2.4 7.5 4.6" fill="none" stroke="currentColor" stroke-width="1"/><circle cx="5" cy="6.6" r="1" fill="currentColor"/></svg></span>
    <span class="time">9:41 AM</span>
    <span class="battery">100% <span class="battery-icon"><span></span></span></span>
  </div>
  <div class="nav-bar">
    <svg class="back" width="9" height="14" viewBox="0 0 9 14"><path d="M7 1 L1.5 7 L7 13" fill="none" stroke="#333" stroke-width="1.4"/></svg>
    Index Details
  </div>
  <div class="index-banner">25 ‘Meaningful’ Brands</div>
  <svg class="chart" viewBox="0 0 270 153" role="img" aria-label="Line chart of index performance against the BM 500 benchmark">
    <g font-size="6.5" fill="#aaa" text-anchor="end">
      <text x="20" y="14">30</text><text x="20" y="31">20</text><text x="20" y="48">10</text>
      <text x="20" y="64">0</text><text x="20" y="81">-10</text><text x="20" y="98">-20</text>
    </g>
    <g stroke="#eee" stroke-width="0.8">
      <line x1="38" y1="29" x2="258" y2="29"/><line x1="38" y1="46" x2="258" y2="46"/>
      <line x1="38" y1="62" x2="258" y2="62"/><line x1="38" y1="79" x2="258" y2="79"/>
      <line x1="38" y1="96" x2="258" y2="96" stroke="#ccc"/>
    </g>
    <g font-size="6.5" fill="#aaa" text-anchor="middle">
      <text x="47" y="106">Aug</text><text x="65" y="106">Sep</text><text x="84" y="106">Oct</text>
      <text x="102" y="106">Nov</text><text x="121" y="106">Dec</text><text x="139" y="106">Jan</text>
      <text x="157" y="106">Feb</text><text x="176" y="106">Mar</text><text x="194" y="106">Apr</text>
      <text x="213" y="106">May</text><text x="231" y="106">Jun</text><text x="249" y="106">Jul</text>
    </g>
    <polyline fill="none" stroke="var(--brand-blue)" stroke-width="1.1" points="40,62 48,62 55,60 62,64 70,60 78,62 86,60 95,66 102,67 110,59 118,56 125,58 132,52 140,54 147,50 152,57 158,49 165,50 172,47 180,49 186,43 193,44 200,47 207,44 214,43 220,45 227,42 234,44 240,40 244,45 248,42 255,43"/>
    <polyline fill="none" stroke="var(--loss)" stroke-width="1.1" points="40,63 48,64 55,69 62,66 70,62 78,64 86,64 95,70 102,73 110,64 118,61 125,63 132,60 140,66 147,58 152,62"/>
    <polyline fill="none" stroke="var(--gain)" stroke-width="1.1" points="152,62 158,56 165,58 172,52 180,56 186,50 193,52 200,48 207,47 214,46 220,49 227,45 234,47 240,44 244,48 248,49"/>
    <polyline fill="none" stroke="var(--loss)" stroke-width="1.1" points="248,49 252,52 255,54"/>
    <rect x="37" y="118" width="14" height="4" rx="2" fill="none" stroke="var(--loss)" stroke-width="0.9"/>
    <rect x="44" y="118" width="21" height="4" rx="2" fill="none" stroke="var(--gain)" stroke-width="0.9"/>
    <text x="68" y="122" font-size="6.5" fill="#999">Index performance</text>
    <rect x="37" y="130" width="28" height="4" rx="2" fill="none" stroke="var(--brand-blue)" stroke-width="0.9"/>
    <text x="68" y="134" font-size="6.5" fill="#999">BM 500 performance</text>
  </svg>
  <nav class="tabs">
    <span class="tab">Description</span>
    <span class="tab tab--active">Performance<br>Snapshot</span>
    <span class="tab">Components</span>
  </nav>
  <div class="stats">
    <div class="row"><span>Date Created</span><span>6 Jan 2012</span></div>
    <div class="row"><span>Num of Stocks</span><span>21</span></div>
    <div class="row"><span>Num of Us Stock</span><span>15</span></div>
    <div class="row"><span>Period Return</span><span class="loss">-1.68%</span></div>
    <div class="row"><span>BM500 Return</span><span class="gain">5.24%</span></div>
  </div>
</section>

<section class="screen screen--detail-area">
  <div class="status-bar">
    <span class="signal"><span class="dots">●●●●●</span> Carrier
      <svg width="10" height="8" viewBox="0 0 10 8"><path d="M1 3 Q5 -0.5 9 3 M2.5 4.6 Q5 2.4 7.5 4.6" fill="none" stroke="currentColor" stroke-width="1"/><circle cx="5" cy="6.6" r="1" fill="currentColor"/></svg></span>
    <span class="time">9:41 AM</span>
    <span class="battery">100% <span class="battery-icon"><span></span></span></span>
  </div>
  <div class="nav-bar">
    <svg class="back" width="9" height="14" viewBox="0 0 9 14"><path d="M7 1 L1.5 7 L7 13" fill="none" stroke="#333" stroke-width="1.4"/></svg>
    Index Details
  </div>
  <div class="index-banner">25 ‘Meaningful’ Brands</div>
  <svg class="chart" viewBox="0 0 270 153" role="img" aria-label="Area chart of index performance against the BM 500 benchmark">
    <g font-size="6.5" fill="#aaa" text-anchor="end">
      <text x="20" y="14">30</text><text x="20" y="31">20</text><text x="20" y="48">10</text>
      <text x="20" y="64">0</text><text x="20" y="81">-10</text><text x="20" y="98">-20</text>
    </g>
    <g stroke="#eee" stroke-width="0.8">
      <line x1="38" y1="29" x2="258" y2="29"/><line x1="38" y1="46" x2="258" y2="46"/>
    </g>
    <polygon fill="var(--bench-fill)" points="40,61 48,61 55,59 62,63 70,58 78,61 86,59 95,63 102,64 110,57 118,55 125,57 132,52 140,53 147,50 152,55 158,49 165,50 172,47 180,48 186,43 193,44 200,46 207,44 214,43 220,45 227,42 234,44 240,40 244,44 248,41 255,42 255,54 248,49 240,44 227,45 214,46 200,48 186,50 172,52 158,56 152,62 140,66 132,60 118,61 102,73 86,64 70,62 55,69 40,63"/>
    <polyline fill="none" stroke="var(--brand-blue)" stroke-width="1.6" points="40,61 48,61 55,59 62,63 70,58 78,61 86,59 95,63 102,64 110,57 118,55 125,57 132,52 140,53 147,50 152,55 158,49 165,50 172,47 180,48 186,43 193,44 200,46 207,44 214,43 220,45 227,42 234,44 240,40 244,44 248,41 255,42"/>
    <polygon fill="var(--loss-fill)" points="40,63 48,64 55,69 62,66 70,62 78,64 86,64 95,70 102,73 110,64 118,61 125,63 132,60 140,66 147,58 152,62 152,96 40,96"/>
    <polygon fill="var(--gain-fill)" points="152,62 158,56 165,58 172,52 180,56 186,50 193,52 200,48 207,47 214,46 220,49 227,45 234,47 240,44 244,48 248,49 248,96 152,96"/>
    <polygon fill="var(--loss-fill)" points="248,49 252,52 255,54 255,96 248,96"/>
    <polyline fill="none" stroke="var(--loss)" stroke-width="1" points="40,63 48,64 55,69 62,66 70,62 78,64 86,64 95,70 102,73 110,64 118,61 125,63 132,60 140,66 147,58 152,62"/>
    <polyline fill="none" stroke="var(--gain)" stroke-width="1" points="152,62 158,56 165,58 172,52 180,56 186,50 193,52 200,48 207,47 214,46 220,49 227,45 234,47 240,44 244,48 248,49"/>
    <polyline fill="none" stroke="var(--loss)" stroke-width="1" points="248,49 252,52 255,54"/>
    <g font-size="6.5" fill="#aaa" text-anchor="middle">
      <text x="47" y="106">Aug</text><text x="65" y="106">Sep</text><text x="84" y="106">Oct</text>
      <text x="102" y="106">Nov</text><text x="121" y="106">Dec</text><text x="139" y="106">Jan</text>
      <text x="157" y="106">Feb</text><text x="176" y="106">Mar</text><text x="194" y="106">Apr</text>
      <text x="213" y="106">May</text><text x="231" y="106">Jun</text><text x="249" y="106">Jul</text>
    </g>
    <rect x="37" y="118" width="14" height="4" rx="2" fill="none" stroke="var(--loss)" stroke-width="0.9"/>
    <rect x="44" y="118" width="21" height="4" rx="2" fill="none" stroke="var(--gain)" stroke-width="0.9"/>
    <text x="68" y="122" font-size="6.5" fill="#999">Index performance</text>
    <rect x="37" y="130" width="28" height="4" rx="2" fill="none" stroke="var(--brand-blue)" stroke-width="0.9"/>
    <text x="68" y="134" font-size="6.5" fill="#999">BM 500 performance</text>
  </svg>
  <nav class="tabs">
    <span class="tab">Description</span>
    <span class="tab tab--active">Performance<br>Snapshot</span>
    <span class="tab">Components</span>
  </nav>
  <div class="stats">
    <div class="row"><span>Date Created</span><span>6 Jan 2012</span></div>
    <div class="row"><span>Num of Stocks</span><span>21</span></div>
    <div class="row"><span>Num of Us Stock</span><span>15</span></div>
    <div class="row"><span>Period Return</span><span class="loss">-1.68%</span></div>
    <div class="row"><span>BM500 Return</span><span class="gain">5.24%</span></div>
  </div>
</section>

</body>
</html>
```